Medical Internet Marketing Company Needs a Site!

We need a new, fresh website for our search engine optimization and social media marketing company. We specialize in helping medical practices, doctors, physicians, and hospitals with their online presence and web ranking. The site should lean towards being suited for these audiences.

We have several examples of website that we like as well as things that we like about them.

Here are sites that we enjoy.

www.brightwavelab.com

It's a good design for the site all around. The videos, buttons, and images are all excellent. They did a fine job.

- We really like their "contact us" side bar and want to include one like it on the secondary pages.

www.corvantis.net

- We don't like the "thickness" of the top navigation bar.
- We like the page colors, easy navigation, and big call to action phone number in the top right corner.

http://www.teluvo.com/

Out of all the examples provided, Teluvo is our favorite and closest look and style to what we are looking for.

- We really like the openness of the design, such as space between the text and background.

- We want a price page in a style very similar to their pricing page with the services listed and check-marks, etc. although we intend to have multiple service package columns much like Corvantis's SEO pricing page.

- The way the video fits into the home page header is very organized, simple, and attention grabbing. We intend to place a slider with videos here.

- We need a page design that will allow for an image slider like Teluvo's Features page.

Here's a great example of a medical internet marketing website: http://www.dermaplex.com/

Target Market(s)

Our target market is doctors, typically male and typically 40-45 years old. I

Industry/Entity Type

Marketing

Requirements
Must have
• The homepage should have a slider in the video. Interior pages should have a video in the very top similar to how they do it on www.brightwavelab.com

The top navigation tabs needed are:
- Home
- Solutions
- Resources
- About
- Why Quelvo
- Contact

The sidebar should have a GREAT call to action in it on interior pages.

There should be one interior page that is similar to this - http://www.teluvo.com/pricing/

There needs to be a page with multiple boxes that take up a row of the web page's body. This page will house all the case studies similar to brightwave lab's: http://www.brightwavelab.com/success-stories/case-studies/ The one exception is we want the case studies to be inside of "boxes" instead of between horizontal lines like brightwave lab's.
Nice to have
• Color, professional, and clean. GREAT use of calls to actions.

```html
<!DOCTYPE html>
<html lang="en">
<head>
<meta charset="utf-8">
<title>Quelvo – Medical Internet Marketing</title>
<link href="https://fonts.googleapis.com/css2?family=Ubuntu:wght@300;400;500;700&family=Dosis:wght@600;700&family=Arimo:wght@400&display=swap" rel="stylesheet">
<style>
:root{
  --header-dark:#15303a;
  --hero-top:#5cc9dc;
  --hero-bottom:#2aa7c4;
  --nav-text:#1d7fb8;
  --green-dark:#4f9a1c;
  --green-text:#5b9a2a;
  --orange-dark:#e98a0c;
  --ink:#222;
  --body-gray:#555;
  --panel-top:#f2f9fd;
  --panel-bottom:#dcf0fa;
  --panel-border:#a9d6ea;
  --footer:#000;
  --footer-text:#c8c8c8;
  --link-blue:#3fa0e0;
}
*{box-sizing:border-box;margin:0;padding:0}
html,body{width:1175px;height:1200px;overflow:hidden;background:#fff}
body{position:relative;font-family:"Ubuntu",sans-serif;color:var(--ink)}

.site-header{position:absolute;left:0;top:0;width:1175px;height:105px;background:linear-gradient(#1b3a45,var(--header-dark))}
.brand{position:absolute;left:119px;top:34px;display:flex;align-items:center;gap:12px}
.brand-mark{width:26px;height:26px;background:#8fd0e4}
.brand-name{font-family:"Ubuntu",sans-serif;font-weight:300;font-size:38px;letter-spacing:3px;color:#b9c2c6;line-height:1}
.call-cta{position:absolute;left:868px;top:29px;width:184px;height:47px;border-radius:3px;background:linear-gradient(#86cf3e,var(--green-dark));border:1px solid #9be05a;color:#fff;text-align:center;font-size:16px;line-height:20px;padding-top:3px}
.call-cta span{display:block;color:#1d2b10;font-size:16px}

.hero{position:absolute;left:0;top:105px;width:1175px;height:413px;background:linear-gradient(var(--hero-top),var(--hero-bottom));overflow:hidden}
.skyline{position:absolute;left:0;bottom:0;width:1175px;height:150px}

.main-nav{position:absolute;left:108px;top:105px;width:958px;height:38px;background:linear-gradient(#fff,#eef2f4);border:1px solid #d3dde2;border-top:none;display:flex}
.main-nav a{display:flex;align-items:center;justify-content:center;color:var(--nav-text);text-decoration:none;font-size:14px;border-right:1px solid #d8dee1}
.main-nav a:last-child{border-right:none}

.video-frame{position:absolute;left:108px;top:194px;width:482px;height:278px;background:#e8ecee;border:1px solid #cfd6da;border-radius:3px;box-shadow:0 2px 6px rgba(0,0,0,.25)}
.video-still{position:absolute;left:7px;top:7px;width:466px;height:229px;background:linear-gradient(100deg,#f4f2ef 0%,#e7e3de 45%,#c9d7e4 100%)}
.play{position:absolute}
.video-bar{position:absolute;left:7px;top:236px;width:466px;height:33px;background:linear-gradient(#2b2b2b,#0d0d0d);color:#fff;font-size:11px}
.slider-arrow{position:absolute;top:311px;width:30px;height:30px;border-radius:50%;background:#111;border:2px solid #5ec7dd}

.hero-copy{position:absolute;left:627px;top:208px;width:440px;color:#fff}
.hero-copy h1{font-family:"Dosis",sans-serif;font-weight:700;font-size:24px;letter-spacing:-.2px;text-shadow:0 1px 2px rgba(0,0,0,.25);line-height:28px}
.hero-copy p{font-size:12px;line-height:18px;margin-top:5px;width:405px}
.signup{position:absolute;left:627px;top:356px;width:238px;height:63px;border-radius:3px;background:linear-gradient(#fbb43a,var(--orange-dark));border:1px solid #ffd27c;text-align:center;color:#fff}
.signup .big{font-family:"Dosis",sans-serif;font-weight:600;font-size:22px;margin-top:8px;line-height:26px}
.signup .big b{font-weight:700;font-size:29px;color:#fff3a8;margin-left:6px}
.signup small{display:block;font-size:11px;margin-top:6px}

.services{position:absolute;left:0;top:540px;width:1175px}
.service{position:absolute;top:0;width:225px}
.service-icon{position:absolute;left:0;top:8px;width:56px;height:56px;border-radius:6px}
.service h2{position:absolute;left:70px;top:17px;font-size:17px;font-weight:700;line-height:24px;color:#1a1a1a}
.service p{position:absolute;left:4px;top:95px;width:205px;font-size:11px;letter-spacing:.6px;line-height:18px;color:var(--body-gray)}
.service a{position:absolute;left:4px;top:180px;color:var(--green-text);font-size:12px;font-weight:500;text-decoration:none;letter-spacing:.4px}
.divider{position:absolute;top:565px;width:1px;height:150px;background:#e3e3e3}

.about-panel{position:absolute;left:108px;top:771px;width:953px;height:256px;border:1px solid var(--panel-border);border-radius:5px;background:linear-gradient(var(--panel-top),var(--panel-bottom))}
.ribbon{position:absolute;left:98px;top:781px;width:175px;height:46px;background:linear-gradient(#88cf45,var(--green-dark));color:#fff;font-size:30px;font-weight:300;letter-spacing:1px;padding-left:28px;line-height:46px;border-radius:2px 3px 3px 0}
.ribbon-fold{position:absolute;left:98px;top:827px;width:0;height:0;border-top:8px solid #3c7512;border-left:8px solid transparent}
.about-copy{position:absolute;left:121px;top:838px;width:631px;font-size:12px;line-height:15.5px;color:#2a2a2a;text-align:justify;letter-spacing:-.2px}
.about-copy p{margin-bottom:15px}
.news-sep{position:absolute;left:776px;top:771px;width:1px;height:256px;background:#d4eaf4}
.news h2{position:absolute;left:800px;top:790px;font-size:29px;font-weight:300;color:#333}
.news h2 b{font-weight:500}
.news-item{position:absolute;left:800px;width:253px}
.news-thumb{position:absolute;left:0;top:0;width:49px;height:49px;background:linear-gradient(#6a5a48,#1e1a18)}
.news-item time{position:absolute;left:55px;top:0;color:var(--green-dark);font-size:11px}
.news-item p{position:absolute;left:55px;top:14px;width:198px;font-size:11px;line-height:14px;text-align:justify;color:#222;letter-spacing:-.2px}

.site-footer{position:absolute;left:0;top:1061px;width:1175px;height:139px;background:var(--footer);font-family:"Arimo",sans-serif;font-size:12px;color:var(--footer-text)}
.site-footer a{color:var(--link-blue);text-decoration:none}
.legal{position:absolute;left:129px;top:18px;line-height:17px}
.share{position:absolute;left:129px;top:68px;display:flex;gap:8px;align-items:center}
.footer-brand{position:absolute;left:703px;top:12px;display:flex;align-items:center;gap:10px}
.footer-brand .brand-name{font-size:31px}
.footer-brand .brand-mark{width:22px;height:22px}
.person{position:absolute;left:705px;top:53px;line-height:17px}
.contact-lines{position:absolute;left:922px;top:53px;line-height:17px}
.contact-lines .blue{color:var(--link-blue)}
</style>
</head>
<body>

<header class="site-header">
  <div class="brand"><span class="brand-mark"></span><span class="brand-name">QUELVO</span></div>
  <div class="call-cta">Contact Us Today<span>(555) 318-4702</span></div>
</header>

<section class="hero">
  <svg class="skyline" viewBox="0 0 1175 150" role="img" aria-label="City skyline silhouette" preserveAspectRatio="none">
    <defs><linearGradient id="sky" x1="0" y1="0" x2="0" y2="1"><stop offset="0" stop-color="#2f9cba" stop-opacity=".5"/><stop offset="1" stop-color="#2590ad"/></linearGradient></defs>
    <rect x="0" y="30" width="1175" height="120" fill="url(#sky)"/>
  </svg>
</section>

<nav class="main-nav">
  <a href="#" style="width:116px">Home</a>
  <a href="#" style="width:177px">Solutions</a>
  <a href="#" style="width:168px">Resources</a>
  <a href="#" style="width:147px">About</a>
  <a href="#" style="width:186px">Why Quelvo</a>
  <a href="#" style="width:164px">Contact</a>
</nav>

<div class="slider-arrow" style="left:91px"></div>
<div class="slider-arrow" style="left:580px"></div>

<div class="video-frame">
  <div class="video-still" role="img" aria-label="Video still of a doctor with a stethoscope and medical staff with a patient in the background"></div>
  <svg class="play" width="70" height="70" viewBox="0 0 70 70" style="left:219px;top:87px"><circle cx="35" cy="35" r="35" fill="#555" fill-opacity=".8"/><path d="M27 20 L52 35 L27 50Z" fill="#ddd"/></svg>
  <div class="video-bar">
    <svg width="466" height="33" viewBox="0 0 466 33">
      <path d="M9 11 L17 16.5 L9 22Z" fill="#fff"/>
      <rect x="27" y="14" width="248" height="5" rx="2" fill="#333"/>
      <rect x="27" y="14" width="156" height="5" rx="2" fill="#2f8fd0"/>
      <text x="286" y="21" fill="#fff" font-size="11" font-family="Ubuntu,sans-serif">1:26 / <tspan fill="#999">3:22</tspan></text>
      <path d="M352 14 h3 l5 -4 v13 l-5 -4 h-3z" fill="#fff"/>
      <rect x="368" y="14" width="40" height="5" rx="2" fill="#333"/>
      <rect x="368" y="14" width="28" height="5" rx="2" fill="#2f8fd0"/>
      <rect x="420" y="4" width="1" height="25" fill="#444"/>
      <rect x="430" y="11" width="13" height="11" fill="none" stroke="#fff" stroke-width="2"/>
      <text x="446" y="22" fill="#fff" font-size="13" font-weight="700" font-style="italic" font-family="Ubuntu,sans-serif">HD</text>
    </svg>
  </div>
</div>

<div class="hero-copy">
  <h1>MAKE SEO YOUR COMPETITIVE ADVANTAGE</h1>
  <p>Lorem Ipsum is simply dummy text of the printing and typesetting industry. Lorem Ipsum has been the industry's standard dummy text ever since the 1500s, when an unknown printer took a galley of type and scrambled it to make a type specimen book.</p>
</div>
<div class="signup"><div class="big">Sign up for<b>FREE</b></div><small>No credit card required and no obligation</small></div>

<section class="services">
  <article class="service" style="left:137px">
    <div class="service-icon" role="img" aria-label="Colourful bar chart icon" style="background:linear-gradient(90deg,#f07a1e,#f6c31a,#6ab82e)"></div>
    <h2>Reputaion<br>Management</h2>
    <p>Lorem Ipsum is simply dummy text of the printing and..... typesetting industry. Lorem Ipsum has been the industry's standard dummy text ever</p>
    <a href="#">Read More....</a>
  </article>
  <article class="service" style="left:372px">
    <div class="service-icon" role="img" aria-label="Computer monitor and devices icon" style="background:linear-gradient(#6a3fa0,#222)"></div>
    <h2 style="left:75px">Online Reputation<br>Management</h2>
    <p>Lorem Ipsum is simply dummy text of the printing and..... typesetting industry. Lorem Ipsum has been the industry's standard dummy text ever</p>
    <a href="#">Read More....</a>
  </article>
  <article class="service" style="left:622px">
    <div class="service-icon" role="img" aria-label="SEO growth arrows icon" style="background:linear-gradient(#f4a21e,#2f8fd0)"></div>
    <h2 style="left:60px">Online<br>Reputation</h2>
    <p style="width:210px">Lorem Ipsum is simply dummy text of the printing and..... typesetting industry. Lorem Ipsum has been the industry's standard dummy text ever</p>
    <a href="#">Read More....</a>
  </article>
  <article class="service" style="left:845px">
    <div class="service-icon" role="img" aria-label="Green shield icon" style="background:linear-gradient(#9bd04a,#3c7512);border-radius:6px 6px 28px 28px;width:48px"></div>
    <h2 style="left:63px">Brand<br>Protection</h2>
    <p>Lorem Ipsum is simply dummy text of the printing and..... typesetting industry. Lorem Ipsum has been the industry's standard dummy text ever</p>
    <a href="#">Read More....</a>
  </article>
</section>
<span class="divider" style="left:354px"></span>
<span class="divider" style="left:598px"></span>
<span class="divider" style="left:835px"></span>

<section class="about-panel"></section>
<div class="ribbon">QUELVO</div>
<div class="ribbon-fold"></div>
<div class="about-copy">
  <p>Lorem Ipsum is simply dummy text of the printing and typesetting industry. Lorem Ipsum has been the industry's standard dummy text ever since the 1500s, when an unknown printer took a galley of type and scrambled it to make a type specimen book.</p>
  <p>It has survived not only five centuries, but also the leap into electronic typesetting, remaining essentially unchanged. It was popularised in the 1960s with the release of Lettrova sheets containing Lorem Ipsum passages, and more recently with desktop publishing software like Pagewright Studio including versions of Lorem Ipsum.</p>
  <p style="margin-top:23px">Lorem Ipsum is simply dummy text of the printing and typesetting industry. Lorem Ipsum has been the industry's standard dummy text ever since the 1500s, when an unknown printer took a galley of type and scrambled it to make a type specimen book.</p>
</div>
<span class="news-sep"></span>
<aside class="news">
  <h2>Latest <b>News</b></h2>
  <div class="news-item" style="top:836px">
    <div class="news-thumb" role="img" aria-label="Photo of a celebrating business team"></div>
    <time>21-03-2012</time>
    <p>Lorem Ipsum is simply dummy text of the printing and typesetting industry. Lorem Ipsum has been the industry's standard dummy text ever since the 1500s</p>
  </div>
  <div class="news-item" style="top:935px">
    <div class="news-thumb" role="img" aria-label="Photo of a group of business people" style="background:linear-gradient(#c89a4a,#2a2420)"></div>
    <time>21-03-2012</time>
    <p>Lorem Ipsum is simply dummy text of the printing and typesetting industry. Lorem Ipsum has been the industry's standard dummy text ever since the 1500s</p>
  </div>
</aside>

<footer class="site-footer">
  <div class="legal">©2012 QUELVO.&nbsp; All Rights Reserved .Inc<br><a href="#">Terms of Use</a> | <a href="#">Privacy Policy</a></div>
  <div class="share">
    <svg width="14" height="24" viewBox="0 0 14 24"><rect x="1" y="2" width="12" height="20" fill="#fff"/></svg>
    <svg width="34" height="24" viewBox="0 0 34 24"><circle cx="17" cy="12" r="11" fill="#fff"/></svg>
    <svg width="34" height="26" viewBox="0 0 34 26"><rect x="1" y="2" width="32" height="22" fill="none" stroke="#fff" stroke-width="3"/><path d="M1 2 L17 14 L33 2 M1 24 L13 12 M33 24 L21 12" stroke="#fff" stroke-width="3" fill="none"/></svg>
    <svg width="28" height="26" viewBox="0 0 28 26"><rect x="7" y="1" width="14" height="8" fill="#fff"/><rect x="1" y="9" width="26" height="11" rx="2" fill="#fff"/><rect x="7" y="17" width="14" height="8" fill="#fff" stroke="#000" stroke-width="1.5"/></svg>
    <svg width="26" height="26" viewBox="0 0 26 26"><rect x="10" y="1" width="6" height="24" fill="#fff"/><rect x="1" y="10" width="24" height="6" fill="#fff"/></svg>
  </div>
  <div class="footer-brand"><span class="brand-mark"></span><span class="brand-name">QUELVO</span></div>
  <div class="person">DANA WHITCOMBE<br>Cheif Executive Officer<br>Quelvo, LLC</div>
  <div class="contact-lines">www.Quelvo.com<br>www.DanaWhitcombe.com<br><span class="blue">Direct - (555) 318-4702</span><br><span class="blue">Cell - (555) 604-2195</span></div>
</footer>

</body>
</html>
```